Professional Speaker needs a Business Card Design

I am a Professional Speaker and I need a design for my business cards. I would like for it to look sleek and professional but not too busy or cluttered. The colors I need are a bright blue, middle level gray and white. I also want a picture on both the front and back of the card. I have somewhat of a design that I created but it's something very basic. I was having an issue with submitting my images to Kelmo Press because they weren't able to get me the exact colors I wanted. I would like to stick with something similar to what I came up with but am open to viewing your ideas.
Updates
Project Deadline Extended Reason: I've only received designs from a few designers. I would like to see some more options before I make my final decision. Added Thursday, January 08, 2015
Industry/Entity Type
Business
Contact Information for Business Card
Please refer to word document attached. It should be file 5 and that contains all of the details I need on my card. Also please be sure and use my Logo that is attached. The file is named logo front.
Look and feel

```html
<!DOCTYPE html>
<html lang="en">
<head>
<meta charset="utf-8">
<title>Daniel Brooks – Business Card</title>
<link href="https://fonts.googleapis.com/css2?family=Sorts+Mill+Goudy&family=Nunito+Sans:wght@400&display=swap" rel="stylesheet">
<style>
  :root {
    --brand-blue: #0a14f0;
    --mid-gray: #6f6f6f;
    --light-gray: #8a8a8a;
    --card-edge: #dedede;
    --white: #ffffff;
    --ink: #111111;
    --serif: "Sorts Mill Goudy", Georgia, serif;
    --sans: "Nunito Sans", Arial, sans-serif;
  }
  * { margin: 0; padding: 0; box-sizing: border-box; }
  html, body { width: 1054px; height: 1200px; overflow: hidden; background: var(--white); }
  .sheet {
    position: relative; width: 1054px; height: 1200px;
    border: 2px solid var(--ink); background: var(--white);
  }
  .card {
    position: absolute; left: 82px; width: 891px; height: 496px;
    border: 1.5px solid var(--card-edge); background: var(--white); overflow: hidden;
  }
  .card--front { top: 66px; }
  .card--back { top: 605px; height: 498px; }

  /* front */
  .logo-mark {
    position: absolute; left: 38px; top: 50px; width: 122px; height: 122px;
    border: 5px solid var(--brand-blue); border-radius: 50%;
  }
  .name {
    position: absolute; left: 166px; top: 52px;
    font-family: var(--serif); font-size: 56px; line-height: 1; color: var(--brand-blue); letter-spacing: 1px;
  }
  .tagline {
    position: absolute; left: 224px; top: 114px;
    font-family: var(--serif); font-size: 35px; line-height: 1; color: var(--mid-gray); letter-spacing: 1px;
  }
  .rule {
    position: absolute; left: 176px; right: 0; top: 162px; height: 2px; background: var(--brand-blue);
  }
  .details {
    position: absolute; left: 0; width: 780px; top: 180px; text-align: center;
    font-family: var(--sans); font-size: 25px; line-height: 36px; color: var(--mid-gray);
  }
  .contact-band {
    position: absolute; left: 0; right: 0; top: 259px; height: 85px; background: var(--brand-blue);
    text-align: center; padding-top: 8px; padding-right: 110px;
    font-family: var(--sans); font-size: 26px; line-height: 34px; color: var(--white);
  }
  .social {
    position: absolute; display: flex; align-items: center; gap: 14px;
    font-family: var(--sans); font-size: 26px; color: var(--light-gray);
  }
  .social__icon { width: 44px; height: 44px; border-radius: 7px; background: var(--light-gray); }
  .portrait-standing {
    position: absolute; left: 668px; top: 28px; width: 163px; height: 446px;
    background: linear-gradient(180deg, #c9cbe0 0%, #b9bccf 45%, #2a2a2e 60%, #141416 100%);
    border-radius: 30px 30px 8px 8px;
  }

  /* back */
  .motto {
    position: absolute; left: 0; right: 0; top: 40px; text-align: center;
    font-family: var(--serif); font-size: 86px; line-height: 1; letter-spacing: 3px; color: var(--brand-blue);
  }
  .motto .motto__gray { color: var(--light-gray); }
  .portrait-speaking {
    position: absolute; left: 242px; top: 103px; width: 397px; height: 262px;
    background: linear-gradient(180deg, #e9e6ee 0%, #cfccd8 100%);
    border-radius: 120px 120px 0 0;
  }
  .roles-band {
    position: absolute; left: 0; right: 0; top: 365px; height: 128px; background: var(--brand-blue);
    text-align: center; padding-top: 26px;
    font-family: var(--sans); font-size: 52px; line-height: 1.2; color: var(--white); letter-spacing: 1px;
  }
  .roles-line { position: absolute; left: 0; right: 0; bottom: 0; height: 2px; background: var(--brand-blue); }
</style>
</head>
<body>
<div class="sheet">
  <section class="card card--front">
    <div class="logo-mark"></div>
    <div class="name">Daniel Brooks</div>
    <div class="tagline">Forward Thinking</div>
    <div class="rule"></div>
    <div class="details">
      <p>CEO Brooks Horizons</p>
      <p>www.DanielBrooksLive.com</p>
    </div>
    <div class="contact-band">
      <p>hello@danielbrookslive.com</p>
      <p>555.204.3817</p>
    </div>
    <div class="social" style="left:88px; top:374px;"><span class="social__icon"></span>Daniel Brooks</div>
    <div class="social" style="left:88px; top:422px;"><span class="social__icon"></span>D.Brooks22</div>
    <div class="social" style="left:386px; top:374px;"><span class="social__icon"></span>DanielBrooks22</div>
    <div class="social" style="left:386px; top:422px;"><span class="social__icon"></span>Daniel Brooks</div>
    <div class="portrait-standing" role="img" aria-label="Full-length photo of the speaker standing in a checked shirt and dark trousers"></div>
  </section>

  <section class="card card--back">
    <div class="motto">LOVE · <span class="motto__gray">LIVE</span> · LIFE</div>
    <div class="portrait-speaking" role="img" aria-label="Photo of the speaker talking into a microphone"></div>
    <div class="roles-band">SPEAKER · AUTHOR · COACH</div>
    <div class="roles-line"></div>
  </section>
</div>
</body>
</html>
```